New Website for ReBranded Company - CrewBeacon

We have a successful company and website currently but it is a little dated. We have re-branded the company from Harbor Signal Networks to CrewBeacon and have a new logo for the new name. We are looking to build a newer fresher website with the new name. I will need a concept of the home page and one inside page. You can see our current site at https://www.harborsignalnetworks.example and the new site will be https://www.crewbeacon.example .

I also really like the https://www.pathlantern.example/ website. I like ledgerkite.example website. I like the https://skillorbit.example/ website.

See the attached document for layout and some text to use. Use the pictures I attached as opposed to pictures from the old site as much as you can.

Target Market(s)

Business

Industry/Entity Type

Software Service

Number of Pages Required

2 page

Font styles to use
Sans Serif

Requirements
Must have
• Use the colors from my logo. Professional but modern. We want people to feel like our product makes their staff feel safer at work.
Should not have
• Don't use any red or orange (no stop colors).

```html
<!DOCTYPE html>
<html lang="en">
<head>
<meta charset="utf-8">
<title>CrewBeacon – Home</title>
<link href="https://fonts.googleapis.com/css2?family=Montserrat:wght@400;500;600;700;800&display=swap" rel="stylesheet">
<style>
:root{
  --blue:#3a96d4;
  --green:#7ab648;
  --navy:#34495e;
  --navy-deep:#1f2c3d;
  --ink:#2f4052;
  --text:#3d4a57;
  --muted:#6b7785;
  --white:#ffffff;
  --line:#e6e9ec;
}
*{margin:0;padding:0;box-sizing:border-box}
html,body{width:1200px;height:3995px;overflow:hidden;background:var(--white)}
body{font-family:'Montserrat',sans-serif;color:var(--text);position:relative}
.abs{position:absolute}
.center{text-align:center}

/* header */
.site-header{position:absolute;left:0;top:0;width:1200px;height:87px;background:var(--white)}
.brand{position:absolute;display:flex;align-items:center;gap:10px;font-weight:700;color:var(--blue)}
.brand-dot{width:30px;height:30px;border-radius:50%;background:var(--blue)}
.site-header .brand{left:81px;top:22px;font-size:26px}
.nav{position:absolute;top:36px;font-size:12px;color:var(--text)}
.login-btn{position:absolute;left:930px;top:29px;width:170px;height:35px;background:var(--green);color:var(--white);font-size:12px;font-weight:500;display:flex;align-items:center;justify-content:center;gap:7px;letter-spacing:.3px}

/* hero */
.hero{position:absolute;left:0;top:87px;width:1200px;height:521px;background:linear-gradient(100deg,#33475f 0%,#26374c 45%,#1b2838 100%)}
.hero h1{position:absolute;left:82px;top:112px;width:420px;font-size:45px;font-weight:800;line-height:47px;color:var(--white);letter-spacing:-.5px}
.hero p{position:absolute;left:82px;top:280px;width:400px;font-size:21px;line-height:26px;color:var(--white)}
.btn-solid{position:absolute;background:var(--blue);color:var(--white);font-size:11.5px;font-weight:500;display:flex;align-items:center;justify-content:center;letter-spacing:.3px}
.hero .btn-solid{left:85px;top:359px;width:250px;height:50px}
.hero-video{position:absolute;left:535px;top:111px;width:560px;height:315px;background:linear-gradient(135deg,#c9d3dc,#8ea0b0 55%,#5f7284);display:flex;align-items:center;justify-content:center}

/* features */
.features{position:absolute;left:0;top:608px;width:1200px;height:276px}
.feature{position:absolute;top:0;height:276px;color:var(--white);text-align:center;font-size:15.5px;line-height:26px}
.feature svg{position:absolute;top:43px;left:50%;transform:translateX(-50%)}
.feature p{position:absolute;top:147px;left:0;right:0;margin:0 auto}

/* headings */
.section-title{position:absolute;left:0;width:1200px;text-align:center;font-weight:700;color:var(--navy);font-size:50px;letter-spacing:1px;line-height:62px}
.lead{position:absolute;left:0;width:1200px;text-align:center;font-size:15px;line-height:26px;color:var(--text)}
.btn-outline{position:absolute;border:1.5px solid var(--blue);color:var(--blue);font-size:11.5px;display:flex;align-items:center;justify-content:center;letter-spacing:.3px;background:var(--white)}

/* why */
.why-col{position:absolute;text-align:center}
.why-col h3{font-size:20px;font-weight:600;color:var(--navy);line-height:26px;letter-spacing:.5px}
.why-col p{margin-top:32px;font-size:15.5px;line-height:26px;color:var(--text)}
.why-card{position:absolute;left:425px;top:1556px;width:350px;height:315px;background:var(--blue);border-radius:6px;box-shadow:0 10px 24px rgba(0,0,0,.2);color:var(--white)}
.why-card .dash{position:absolute;inset:12px;border:2px dashed rgba(255,255,255,.75)}
.why-card h3{position:absolute;top:50px;left:0;width:100%;text-align:center;font-size:20px;font-weight:600;line-height:26px}
.why-card .intro{position:absolute;top:128px;left:60px;font-size:15.5px}
.options{position:absolute;top:170px;left:60px;width:240px;display:grid;grid-template-columns:1fr 1fr;row-gap:0;font-size:15.5px;line-height:26px}
.options span:nth-child(odd){padding-left:0}
.options .c{text-align:center}

/* band */
.band-green{position:absolute;left:0;top:2087px;width:1200px;height:210px;background:linear-gradient(90deg,#76b143,#7fbb4c);color:var(--white)}
.band-green .txt{position:absolute;font-size:14.5px;line-height:25px;text-align:center}
.btn-ghost{position:absolute;border:1.5px solid var(--white);color:var(--white);font-size:11.5px;display:flex;align-items:center;justify-content:center}
.stats{position:absolute;left:624px;top:112px;display:flex;align-items:baseline;font-size:20px}
.stats b{font-size:28px;font-weight:700;margin-right:8px}
.stats small{font-size:14px;margin:0 38px 0 32px}

/* plan */
.plan-card{position:absolute;top:2545px;width:317px;height:397px;background:var(--white);box-shadow:0 3px 14px rgba(0,0,0,.08);text-align:center}
.plan-card .dash{position:absolute;inset:12px;border:1.5px dashed #d7dce1}
.plan-card svg{position:absolute;top:31px;left:50%;transform:translateX(-50%)}
.plan-card h3{position:absolute;top:188px;left:0;width:100%;font-size:20px;font-weight:600;color:var(--navy);line-height:26px}
.plan-card ul{position:absolute;top:268px;list-style:none;font-size:15.5px;line-height:26px;text-align:left;color:var(--text)}
.plan-card ul li::before{content:"• "}
.plan-card .note{position:absolute;top:268px;left:30px;right:30px;font-size:15.5px;line-height:26px;color:var(--text)}

/* cta band */
.band-dark{position:absolute;left:0;top:3202px;width:1200px;height:211px;background:linear-gradient(90deg,#3a4e67 0%,#465c75 55%,#34475e 100%)}
.band-dark h2{position:absolute;left:78px;top:74px;font-size:34px;line-height:42px;font-weight:800;color:var(--white)}
.btn-green{position:absolute;left:868px;top:89px;width:175px;height:49px;background:var(--green);color:var(--white);font-size:11.5px;display:flex;align-items:center;justify-content:center}

/* footer */
.footer-contact{position:absolute;left:113px;top:3505px;width:300px}
.footer-contact .label{font-size:20px;font-weight:500;color:var(--navy)}
.footer-contact .phone{font-size:28px;font-weight:600;color:var(--navy);line-height:32px;letter-spacing:.5px}
.footer-contact p{margin-top:30px;font-size:15px;line-height:26px;color:var(--text)}
.footer-col{position:absolute;top:3500px}
.footer-col h4{font-size:20px;font-weight:600;color:var(--navy);letter-spacing:.5px}
.footer-col .rule{width:52px;height:2px;background:var(--blue);margin-top:16px;margin-bottom:14px}
.footer-col ul{list-style:none}
.footer-col li{font-size:15.5px;line-height:38.8px;color:var(--text);display:flex;align-items:center;gap:12px}
.footer-col li svg{flex:none}
.footer-rule{position:absolute;left:113px;top:3875px;width:975px;height:1px;background:var(--line)}
.footer-brand{left:116px;top:3904px;font-size:28px}
.copyright{position:absolute;left:894px;top:3920px;font-size:15.5px;color:var(--text)}
</style>
</head>
<body>

<header class="site-header">
  <div class="brand"><span class="brand-dot"></span>CrewBeacon</div>
  <span class="nav" style="left:700px">Home</span>
  <span class="nav" style="left:775px">Buy Addons</span>
  <svg class="abs" style="left:883px;top:33px" width="20" height="20" viewBox="0 0 20 20"><circle cx="8" cy="8" r="6.5" fill="none" stroke="#3d4a57" stroke-width="1.6"/><line x1="13" y1="13" x2="18.5" y2="18.5" stroke="#3d4a57" stroke-width="1.6"/></svg>
  <div class="login-btn">
    <svg width="12" height="13" viewBox="0 0 12 13"><circle cx="6" cy="3.6" r="2.8" fill="none" stroke="#fff" stroke-width="1.2"/><path d="M1 12.5c0-3 2.2-5 5-5s5 2 5 5" fill="none" stroke="#fff" stroke-width="1.2"/></svg>
    CUSTOMER LOGIN
  </div>
</header>

<section class="hero" role="img" aria-label="Background photo of a hand holding a handheld panic button">
  <h1>Feel Confident that your Staff is protected</h1>
  <p>Get a revolutionary new electronic panic button</p>
  <div class="btn-solid">READY TO GET STARTED</div>
  <div class="hero-video" role="img" aria-label="Video thumbnail of a smiling group of coworkers">
    <svg width="70" height="70" viewBox="0 0 70 70"><circle cx="35" cy="35" r="31" fill="rgba(0,0,0,.15)" stroke="#fff" stroke-width="5"/><path d="M27 20l24 15-24 15z" fill="#fff"/></svg>
  </div>
</section>

<section class="features">
  <div class="feature" style="left:0;width:397px;background:linear-gradient(135deg,#3c98d6,#2f86c4)" role="img" aria-label="Blue tinted photo of a hand pressing a button">
    <svg width="80" height="80" viewBox="0 0 80 80" fill="none" stroke="#fff" stroke-width="3.5"><circle cx="40" cy="40" r="12"/><path d="M34 6h12l2 9 8 4 8-5 8 8-5 8 4 8 9 2v12l-9 2-4 8 5 8-8 8-8-5-8 4-2 9H34l-2-9-8-4-8 5-8-8 5-8-4-8-9-2V34l9-2 4-8-5-8 8-8 8 5 8-4z"/></svg>
    <p style="width:250px">Problems Stopped Before They Start For Any Type Of Organization</p>
  </div>
  <div class="feature" style="left:397px;width:381px;background:linear-gradient(135deg,#7cb84a,#6fa93f)" role="img" aria-label="Green tinted photo of a phone handset">
    <svg width="80" height="60" viewBox="0 0 80 60" fill="none" stroke="#fff" stroke-width="3.5"><path d="M5 6h52l18 24-18 24H5z"/></svg>
    <p style="width:250px">Affordable Prices Starting at $18 per month. No Contracts. No Hidden Costs.</p>
  </div>
  <div class="feature" style="left:778px;width:422px;background:linear-gradient(135deg,#3d5069,#2e3f55)" role="img" aria-label="Dark tinted photo of an office desk phone">
    <svg width="80" height="78" viewBox="0 0 80 78" fill="none" stroke="#fff" stroke-width="3.5" stroke-linejoin="round"><path d="M40 4l10.5 23 25 2.5-19 17 5.5 25L40 59 18 71.5l5.5-25-19-17 25-2.5z"/></svg>
    <p style="width:230px">Alerts by computer, mobile device, text, phone, email, monitoring and E911</p>
  </div>
</section>

<h2 class="section-title" style="top:1015px">YOUR EMPOYEES SHOULDN’T<br>FEEL ALONE WHEN THEY NEED HELP</h2>
<p class="lead" style="top:1165px">Does this problem make you feel frustrated and anxious?<br>Put a simple solution in their hands</p>
<div class="btn-outline" style="left:476px;top:1266px;width:251px;height:51px">READY TO GET STARTED</div>

<h2 class="section-title" style="top:1426px">WHY BUSINESSES CHOOSE US</h2>

<div class="why-col" style="left:118px;top:1607px;width:250px">
  <h3>EASY TO<br>USE</h3>
  <p>Press a button and let the right people know you need help and open a chat window letting everyone talk on resolving their problem.</p>
</div>
<div class="why-card">
  <div class="dash"></div>
  <h3>COMMUNICATE THE WAY<br>YOU WANT</h3>
  <div class="intro">We give you lots of options:</div>
  <div class="options">
    <span>Computer</span><span class="c">Text</span>
    <span style="padding-left:12px">Mobile</span><span class="c">E911</span>
    <span style="padding-left:18px">Email</span><span class="c">Call Center</span>
    <span>Phone call</span><span></span>
  </div>
</div>
<div class="why-col" style="left:822px;top:1607px;width:250px">
  <h3>COST EFFECTIVE<br>PROTECTION</h3>
  <p>By leveraging your existing network and equipment we can lower your costs to give better options to your staff.</p>
</div>
<div class="btn-outline" style="left:476px;top:1936px;width:251px;height:51px">READY TO GET STARTED</div>

<section class="band-green" role="img" aria-label="Green tinted office photo background">
  <div class="txt" style="left:133px;top:46px;width:360px">We know how scary it can feel to worry about employee safety.</div>
  <div class="btn-ghost" style="left:225px;top:122px;width:176px;height:51px">START MY DEMO</div>
  <div class="txt" style="left:589px;top:46px;width:440px">That’s why we have provided a way for customers to get help to staff effectively in</div>
  <div class="stats"><b>45</b>States<small>covering</small><b>5</b>Countries</div>
</section>

<h2 class="section-title" style="top:2404px">SIMPLE START PLAN</h2>

<div class="plan-card" style="left:96px">
  <div class="dash"></div>
  <svg width="100" height="117" viewBox="0 0 100 117"><path d="M50 2L98 20v36c0 30-22 50-48 59C24 106 2 86 2 56V20z" fill="#3a96d4"/><text x="50" y="74" text-anchor="middle" font-family="Montserrat,sans-serif" font-size="44" font-weight="700" fill="#fff">1</text></svg>
  <h3>Explore Your<br>Choices</h3>
  <ul style="left:85px"><li>Pricing</li><li>Trial</li><li>Quote</li><li>Hardware</li></ul>
</div>
<div class="plan-card" style="left:443px">
  <div class="dash"></div>
  <svg width="100" height="117" viewBox="0 0 100 117"><path d="M50 2L98 20v36c0 30-22 50-48 59C24 106 2 86 2 56V20z" fill="#7ab648"/><text x="50" y="74" text-anchor="middle" font-family="Montserrat,sans-serif" font-size="44" font-weight="700" fill="#fff">2</text></svg>
  <h3>Get Setup</h3>
  <ul style="left:69px"><li>Input Your Alerts</li><li>Input Your Staff</li><li>Install Our Software</li></ul>
</div>
<div class="plan-card" style="left:797px">
  <div class="dash"></div>
  <svg width="100" height="117" viewBox="0 0 100 117"><path d="M50 2L98 20v36c0 30-22 50-48 59C24 106 2 86 2 56V20z" fill="#34495e"/><text x="50" y="74" text-anchor="middle" font-family="Montserrat,sans-serif" font-size="44" font-weight="700" fill="#fff">3</text></svg>
  <h3>Feel Confident Your<br>Staff Is Protected</h3>
  <p class="note">High Five. You just too a major step to getting rid of the anxiety and frustration this gave you.</p>
</div>
<div class="btn-solid" style="left:476px;top:3007px;width:253px;height:51px">START MY DEMO</div>

<section class="band-dark" role="img" aria-label="Dark blue tinted photo of an office desk phone keypad">
  <h2>Stay Connected with Staff during<br>a Crisis Situations</h2>
  <div class="btn-green">START MY DEMO</div>
</section>

<footer>
  <div class="footer-contact">
    <div class="label">Call Us</div>
    <div class="phone">1 - 800 - 555 - 0147</div>
    <p>When employees feel alone during a threatening situation, we give them a way to let the right resources know that they need help so you can feel confident that your staff is protected.</p>
  </div>

  <div class="footer-col" style="left:484px">
    <h4>SHOP</h4><div class="rule"></div>
    <ul>
      <li><svg width="13" height="11" viewBox="0 0 13 11"><path d="M1 6l4 4 7-9" fill="none" stroke="#3a96d4" stroke-width="1.6"/></svg>Add Ons</li>
      <li><svg width="13" height="11" viewBox="0 0 13 11"><path d="M1 6l4 4 7-9" fill="none" stroke="#3a96d4" stroke-width="1.6"/></svg>Start My Demo</li>
      <li><svg width="13" height="11" viewBox="0 0 13 11"><path d="M1 6l4 4 7-9" fill="none" stroke="#3a96d4" stroke-width="1.6"/></svg>Custom Quote</li>
      <li><svg width="13" height="11" viewBox="0 0 13 11"><path d="M1 6l4 4 7-9" fill="none" stroke="#3a96d4" stroke-width="1.6"/></svg>Start Trial</li>
    </ul>
  </div>
  <div class="footer-col" style="left:684px">
    <h4>ABOUT</h4><div class="rule"></div>
    <ul>
      <li><svg width="13" height="11" viewBox="0 0 13 11"><path d="M1 6l4 4 7-9" fill="none" stroke="#3a96d4" stroke-width="1.6"/></svg>Affiliates</li>
      <li><svg width="13" height="11" viewBox="0 0 13 11"><path d="M1 6l4 4 7-9" fill="none" stroke="#3a96d4" stroke-width="1.6"/></svg>Contact</li>
      <li><svg width="13" height="11" viewBox="0 0 13 11"><path d="M1 6l4 4 7-9" fill="none" stroke="#3a96d4" stroke-width="1.6"/></svg>Support</li>
      <li><svg width="13" height="11" viewBox="0 0 13 11"><path d="M1 6l4 4 7-9" fill="none" stroke="#3a96d4" stroke-width="1.6"/></svg>Existing Customers</li>
      <li><svg width="13" height="11" viewBox="0 0 13 11"><path d="M1 6l4 4 7-9" fill="none" stroke="#3a96d4" stroke-width="1.6"/></svg>Industries</li>
      <li><svg width="13" height="11" viewBox="0 0 13 11"><path d="M1 6l4 4 7-9" fill="none" stroke="#3a96d4" stroke-width="1.6"/></svg>Blog</li>
      <li><svg width="13" height="11" viewBox="0 0 13 11"><path d="M1 6l4 4 7-9" fill="none" stroke="#3a96d4" stroke-width="1.6"/></svg>FAQ</li>
    </ul>
  </div>
  <div class="footer-col" style="left:899px">
    <h4>LEGAL</h4><div class="rule"></div>
    <ul>
      <li><svg width="13" height="11" viewBox="0 0 13 11"><path d="M1 6l4 4 7-9" fill="none" stroke="#3a96d4" stroke-width="1.6"/></svg>Privacy Policy</li>
      <li><svg width="13" height="11" viewBox="0 0 13 11"><path d="M1 6l4 4 7-9" fill="none" stroke="#3a96d4" stroke-width="1.6"/></svg>Terms of Use</li>
      <li><svg width="13" height="11" viewBox="0 0 13 11"><path d="M1 6l4 4 7-9" fill="none" stroke="#3a96d4" stroke-width="1.6"/></svg>End User License</li>
      <li><svg width="13" height="11" viewBox="0 0 13 11"><path d="M1 6l4 4 7-9" fill="none" stroke="#3a96d4" stroke-width="1.6"/></svg>Agreement</li>
    </ul>
  </div>

  <div class="footer-rule"></div>
  <div class="brand footer-brand"><span class="brand-dot" style="width:34px;height:34px"></span>CrewBeacon</div>
  <div class="copyright">©CrewBeacon 2020</div>
</footer>

</body>
</html>
```